Bright Meadow Party Coaches is excited to bring you Fenwick Valley’s Prime luxury limousine ser...

Leisure TransportationWedding DayWe will make your wedding day special and one to remember. Bright Meadow Party Coaches offers custom wedding transportation packages that are designed around your every need. Call our transportation consultant and learn how we can help you have a stress free and perfectly planned wedding event.PromsWe put safety first and give you piece of mind when we transport your loved ones.Special Occasions Bright Meadow Party Coaches professional chauffeured services will make any special event extraordinary. You will feel safe while our professional chauffeurs drive you in style and luxury.Corporate EventsNorth Coast Event Charters is a leader in professional chauffeured transportation services. Our highly trained staff will take the stress out of getting you to and from your destination. Bright Meadow Party Coaches is dedicated to the highest quality of services. Our top-of-the-line Calder-Voss Tramway is always safety inspected and cleaned before each use. Tours From the ocean to the redwoods, we offer tours to suit your needs.,Airport Service We are business ground travel experts. Our doo-to-door limousine can accommodate up to 10 passengers, and service all private and public airports

Target Market(s)

These brochures are going in motels and restaurants.

Font styles to use
Script

Colors
fed55c

Requirements
Must have
• Gold and black are the business colors. Check brand identity PDF

```html
<!DOCTYPE html>
<html lang="en">
<head>
<meta charset="utf-8">
<title>Bright Meadow Party Coaches – Brochure Inside</title>
<link rel="stylesheet" href="https://fonts.googleapis.com/css2?family=Jost:wght@300;400;500&display=swap">
<style>
  :root{
    --gold:#b08a3a;
    --gold-light:#d2ad5e;
    --ink:#1c1c1c;
    --body:#3a3a3a;
    --paper:#f7f7f6;
    --stage:#e9e9e9;
    --black:#0b0b0b;
  }
  *{box-sizing:border-box;margin:0;padding:0}
  html,body{width:1200px;height:800px;overflow:hidden;background:var(--stage)}
  body{font-family:"Jost",sans-serif;color:var(--body)}
  .brochure{position:absolute;left:123px;top:30px;width:954px;height:740px;display:flex;box-shadow:0 6px 24px rgba(0,0,0,.12)}
  .panel{position:relative;width:318px;height:740px;background:var(--paper);overflow:hidden}
  .panel + .panel{border-left:1px solid #e2e2e2}
  .panel-title{font-weight:400;letter-spacing:.32em;line-height:1.15;text-transform:uppercase}
  .panel-title .lead{display:block;color:var(--ink);font-size:19px}
  .panel-title .sub{display:block;color:var(--gold);font-size:19px}
  .title-rule{width:26px;height:3px;background:var(--gold);border-radius:2px;margin:8px 0 18px}
  .service{margin-bottom:16px}
  .service-name{font-size:13px;font-weight:400;letter-spacing:.26em;color:var(--gold);text-transform:uppercase;margin-bottom:4px}
  .copy{font-size:9.6px;line-height:1.5;font-weight:400;color:var(--body)}
  .copy + .copy{margin-top:14px}
  .panel-content{position:absolute;left:30px;right:26px;top:48px}
  .photo{position:absolute;border-radius:50%;border:2px solid #fff}
  .photo-guests{left:22px;top:560px;width:170px;height:170px;background:radial-gradient(circle at 45% 40%,#8c8a88,#3b3a3a 60%,#1b1b1b)}
  .photo-cabin{left:150px;top:520px;width:150px;height:150px;background:radial-gradient(circle at 55% 45%,#c8a57a,#5a3f7a 55%,#1a1530)}
  .photo-arrival{left:26px;top:420px;width:150px;height:150px;background:radial-gradient(circle at 50% 50%,#6d6d72,#2a2a2e 60%,#7a1a1a)}
  .photo-toast{left:150px;top:372px;width:140px;height:140px;background:radial-gradient(circle at 50% 45%,#e8e2d6,#7c8a64 55%,#2f3a26)}
  .band{position:absolute;left:0;width:100%}
  .panel-right .panel-content{top:28px;right:22px}
  .panel-right .copy{color:#2c2c2c}
</style>
</head>
<body>
<main class="brochure">

  <!-- Leisure panel -->
  <section class="panel panel-left">
    <div class="panel-content">
      <h2 class="panel-title"><span class="lead">Leisure</span><span class="sub">Transportation</span></h2>
      <div class="title-rule"></div>
      <article class="service">
        <h3 class="service-name">Wedding Day</h3>
        <p class="copy">We will make your wedding day special and one to remember! Bright Meadow Party Coaches offers customized wedding transportation packages that are designed around your every need.</p>
      </article>
      <article class="service">
        <h3 class="service-name">Special Event</h3>
        <p class="copy">Bright Meadow Party Coaches professional chauffeured services will make any event extraordinary. You will always feel safe while our professional chauffeur will make sure you arrive in style!</p>
      </article>
      <article class="service">
        <h3 class="service-name">Prom</h3>
        <p class="copy">Bright Meadow Party Coaches is a leader in professional chauffeured transportation services. We put safety first and give you piece of mind when we transport your loved ones.</p>
      </article>
      <article class="service">
        <h3 class="service-name">Tours</h3>
        <p class="copy">From the beaches to the Redwoods, we know the biggest trees and the hidden beaches of Fenwick Valley.</p>
      </article>
    </div>
    <svg class="band" style="top:560px;height:180px" viewBox="0 0 318 180" preserveAspectRatio="none" aria-hidden="true">
      <path d="M0 40 C90 30 200 50 318 30 L318 180 L0 180 Z" fill="var(--gold)"/>
      <path d="M0 70 C100 60 210 80 318 60 L318 180 L0 180 Z" fill="var(--black)"/>
    </svg>
    <div class="photo photo-cabin" role="img" aria-label="Photo: limousine cabin interior with purple lighting and leather seating"></div>
    <div class="photo photo-guests" role="img" aria-label="Photo: group of guests in formal black attire beside a limousine"></div>
    <svg class="band" style="top:520px;height:220px" viewBox="0 0 318 220" aria-hidden="true">
      <path d="M8 200 C20 90 120 20 300 60" fill="none" stroke="var(--gold-light)" stroke-width="1"/>
    </svg>
  </section>

  <!-- Luxury panel -->
  <section class="panel panel-middle">
    <div class="panel-content">
      <h2 class="panel-title"><span class="lead">Luxury</span><span class="sub">Transportation</span></h2>
      <div class="title-rule"></div>
      <p class="copy">Fun Red-Carpet Experience- Make your Event remarkable from start to finish with our luxury transportation service. Our limo van makes getting from point A to point B an absolute blast, with wow-factor entertainment options and a comfortable ride for up to 10 of your closest friends. We treat every guest like the VIP they are, with a true red-carpet experience.</p>
      <p class="copy">Upscale Luxury Features- With the Calder-Voss executive coach, you get the prestige of a limousine, but with the added benefits of full standing headroom, easy access through convenient sliding van door. Luxury is built into every detail, form the full length mirrored ceiling to the plush leather wrap-around seating. Make it a party with the surround sound speakers and 2 big screen TV’s, all with touch pad controls. And enjoy the the illuminated solid-wood bar with complementary champagne, cognac, ice, waters, or bring your own beverages to sip on!</p>
    </div>
    <svg class="band" style="top:500px;height:240px" viewBox="0 0 318 240" preserveAspectRatio="none" role="img" aria-label="Photo: black luxury van parked on a coastal overlook with chauffeur standing beside it">
      <defs>
        <linearGradient id="coastTone" x1="0" y1="0" x2="0" y2="1">
          <stop offset="0" stop-color="#9aa6ab"/>
          <stop offset=".55" stop-color="#4d5552"/>
          <stop offset="1" stop-color="#2c302c"/>
        </linearGradient>
      </defs>
      <path d="M0 70 C110 60 220 20 318 0 L318 240 L0 240 Z" fill="url(#coastTone)"/>
      <path d="M0 70 C110 60 220 20 318 0" fill="none" stroke="var(--gold)" stroke-width="3"/>
    </svg>
    <div class="photo photo-arrival" role="img" aria-label="Photo: guest stepping out of the van onto a red carpet"></div>
    <div class="photo photo-toast" role="img" aria-label="Photo: champagne bottle and glasses on ice"></div>
  </section>

  <!-- Service panel -->
  <section class="panel panel-right">
    <svg class="band" style="top:0;height:740px" viewBox="0 0 318 740" preserveAspectRatio="none" role="img" aria-label="Photos: black van on a coastal road above the sea, and the van driving through a redwood forest">
      <defs>
        <linearGradient id="skyTone" x1="0" y1="0" x2="0" y2="1">
          <stop offset="0" stop-color="#f2f3f3"/>
          <stop offset=".45" stop-color="#cdd2d2"/>
          <stop offset=".75" stop-color="#6f7d6a"/>
          <stop offset="1" stop-color="#3e4a3a"/>
        </linearGradient>
        <linearGradient id="forestTone" x1="0" y1="0" x2="0" y2="1">
          <stop offset="0" stop-color="#4a5a3a"/>
          <stop offset=".6" stop-color="#3a4330"/>
          <stop offset="1" stop-color="#6b6c66"/>
        </linearGradient>
      </defs>
      <rect width="318" height="740" fill="url(#skyTone)"/>
      <path d="M0 470 C90 470 150 420 318 410 L318 740 L0 740 Z" fill="var(--gold)"/>
      <path d="M0 490 C100 490 160 440 318 432 L318 740 L0 740 Z" fill="url(#forestTone)"/>
    </svg>
    <div class="panel-content">
      <p class="copy">Flexible, Customized Service- It’s your big day. We’re here to enhance your event and make it everything you hoped it would be. Which is every ride is customized to your personal needs, and we go above and beyond to make the chauffeur experience streamlined and stress free. Want to take the scenic route to your destination, or decide to make a detour on the night of the event? No problem. We’re flexible, and we promise to do what we can to make it happen!</p>
      <p class="copy">Professional, Accommodating, Reliable Service- we’re really offering more than just a ride. We’re offering peace of mind. We’ll take care of the logistics and details so you can focus on enjoying your day. Your personal chauffeur will make sure you are safe and arrive on time. Just hop in, sit back, and enjoy the ride. With Bright Meadow Party Coaches, you’ll always arrive in style!</p>
    </div>
  </section>

</main>
</body>
</html>
```